Harwick Legal

To update and modernize current business card appearance. Marta's business is based in Melbourne with 4 other lawyers in the firm. Marta travels to the Pilbara in Western Australia approximately 1 week a month as part of the firms legal work. She consults with clients in Newman, Tom Price and Port Hedland. The lawyers work mostly from a home office, apart from court appearances. They have a virtual office in Melbourne city, and use facilities in 3 or 4 other locations around Melbourne. It is important the client's think this is a conventional law firm with a permanent office. Our business structure is a difficult concept for them to grasp. The business has been operational for 3 years, growing from 1 lawyer to 4 lawyers during that time. Our website is www.Harwicklegal.example.au and is currently being upgraded as we are not happy with its content. The logo is currently orange and dark grey but the orange is a difficult colour to reproduce and often turns out "poo" brown when documents are printed. We need clients to know we are user friendly and caring - and not head up our rears ends as some lawyers appear to be.
Updates

Thank you for the feedback so far. 1. Some of the designs have too much black (We prefer darker grey & not too much.) 2. Happy for designers to play around with different colours & logo design. What we're after is a modern look and business card that people say "wow" when they pick it up.

Industry/Entity Type

Business

```html
<!DOCTYPE html>
<html lang="en">
<head>
<meta charset="utf-8">
<title>Harwick Legal – Business Card</title>
<link rel="stylesheet" href="https://fonts.googleapis.com/css2?family=Anton&family=Fira+Mono&family=Arimo&display=swap">
<style>
  :root {
    --ink: #000000;
    --paper: #ffffff;
    --guide: #dcdcdc;
  }
  * { margin: 0; padding: 0; box-sizing: border-box; }
  html, body { width: 1200px; height: 1000px; overflow: hidden; background: var(--paper); }
  .sheet { position: relative; width: 1200px; height: 1000px; color: var(--ink); }
  .card { position: absolute; left: 21px; width: 725px; height: 461px; border: 3px solid var(--ink); }
  .card--front { top: 11px; }
  .card--back { top: 500px; }
  .overlay { position: absolute; inset: 0; pointer-events: none; }

  .mono { position: absolute; font-family: "Fira Mono", Monaco, monospace; font-weight: 400; white-space: nowrap; line-height: 1; color: var(--ink); }

  .brand-name { font-size: 20px; }

  .slogan { position: absolute; font-family: "Anton", Impact, sans-serif; font-size: 16px; line-height: 1; white-space: nowrap; }
  .slogan--front { letter-spacing: 2px; }
  .slogan--back { letter-spacing: 2.9px; }

  .contact__name { font-size: 18px; }
  .contact__quals { font-size: 8.7px; }
  .contact__role { font-size: 11.4px; }
  .contact__line { font-size: 9px; }
  .contact__label { display: inline-block; width: 43px; }

  .practice__heading { font-size: 11.8px; }
  .practice__area { font-size: 12px; }
  .practice__detail { font-size: 9px; }

  .marker { position: absolute; font-family: "Arimo", Arial, sans-serif; font-size: 31px; line-height: 1; }
  .legend { position: absolute; left: 778px; top: 124px; font-family: "Arimo", Arial, sans-serif; }
  .legend__title { font-size: 23px; font-weight: 400; margin-bottom: 28px; }
  .legend__list { list-style: none; font-size: 15.5px; line-height: 20px; }
  .legend__gap { height: 20px; }
</style>
</head>
<body>
<div class="sheet">

  <div class="card card--front"></div>
  <div class="card card--back"></div>

  <svg class="overlay" width="1200" height="1000" viewBox="0 0 1200 1000" aria-hidden="true">
    <g fill="none" stroke="var(--guide)" stroke-width="3">
      <path d="M110 230 H86 V485"/>
      <path d="M353 325 H123 V485"/>
      <path d="M642 321 H453 V485"/>
      <path d="M183 868 H108 V1000"/>
      <path d="M367 728 H337 V1000"/>
      <path d="M645 866 H488 V1000"/>
    </g>
    <g fill="none" stroke="var(--ink)" stroke-width="3">
      <rect x="118" y="198" width="282" height="98"/>
      <rect x="373" y="631" width="282" height="205"/>
    </g>
  </svg>

  <!-- Front -->
  <div class="mono brand-name" style="left:134px; top:214px;">Harwick Legal</div>
  <div class="slogan slogan--front" style="left:119px; top:302px;">serving the people of the pilbarra</div>

  <div class="mono contact__name" style="left:457px; top:185px;">J.Marta Ashford</div>
  <div class="mono contact__quals" style="left:457px; top:208px;">llb (hons) - accredited mediator</div>
  <div class="mono contact__role" style="left:457px; top:230px;">Principal Solicitor</div>
  <div class="mono contact__line" style="left:457px; top:272px;"><span class="contact__label">L:</span>1300 Harwick (427 942)</div>
  <div class="mono contact__line" style="left:457px; top:287px;"><span class="contact__label">Mob :</span>0491 570 156</div>
  <div class="mono contact__line" style="left:457px; top:302px;">Email : martaashford@harwicklegal.example.au</div>

  <!-- Back -->
  <div class="mono contact__line" style="left:102px; top:851px;">martaashford@harwicklegal.example.au</div>

  <div class="mono brand-name" style="left:437px; top:650px;">Harwick Legal</div>
  <div class="mono practice__heading" style="left:437px; top:697px;">Area Of Practise:</div>
  <div class="mono practice__area" style="left:437px; top:726px;">- Family Law</div>
  <div class="mono practice__detail" style="left:447px; top:744px;">Colloborative Practice</div>
  <div class="mono practice__detail" style="left:447px; top:759px;">Mediation &amp; Negotiation</div>
  <div class="mono practice__area" style="left:437px; top:786px;">- Criminal Law</div>
  <div class="slogan slogan--back" style="left:380px; top:842px;">experience support solutions</div>

  <!-- Markers -->
  <div class="marker" style="left:97px; top:472px;">1</div>
  <div class="marker" style="left:123px; top:472px;">2</div>
  <div class="marker" style="left:457px; top:472px;">3</div>
  <div class="marker" style="left:109px; top:972px;">4</div>
  <div class="marker" style="left:342px; top:972px;">5</div>
  <div class="marker" style="left:499px; top:972px;">6</div>

  <!-- Legend -->
  <div class="legend">
    <h2 class="legend__title">Legenda:</h2>
    <ul class="legend__list">
      <li>1. New logo (font Impact)</li>
      <li>2. Slogan for the front</li>
      <li>3. Adres box text ,who, what, where.( font Monaco)</li>
      <li class="legend__gap"></li>
      <li>4. Email for the back of the card</li>
      <li>5. Text box for the specialities</li>
      <li>6. Slogan for the back of the card</li>
    </ul>
  </div>

</div>
</body>
</html>
```